Business Card for Holistic Health Business
Bright Ferns Natural Wellness & Live Cell Review
Use same font as used in my logo
Not sure, I am open to different fonts.
Simple
Marla Dunwoody
DynBC, CH, BA
Larkvale Acupuncture Clinic
2736-18 Avenue, Suite 200
Larkvale, AB T8K 2P6
brightferns@mailnest.ca
www.brightfernsnaturalwellness.com
Logo for Bright Ferns business card.

```html
<!DOCTYPE html>
<html lang="en">
<head>
<meta charset="utf-8">
<title>Bright Ferns Business Card</title>
<link rel="stylesheet" href="https://fonts.googleapis.com/css2?family=Open+Sans:wght@400;600&display=swap">
<style>
  :root {
    --bg: #dcdcdc;
    --card: #ffffff;
    --frame: #0b0b0b;
    --ink: #1e1e1e;
    --muted: #6b6b6b;
    --accent: #3f8fd0;
    --rule: #9a9a9a;
  }
  * { margin: 0; padding: 0; box-sizing: border-box; }
  html, body { width: 1200px; height: 895px; overflow: hidden; }
  body {
    background: var(--bg);
    font-family: "Open Sans", Arial, sans-serif;
    color: var(--ink);
    position: relative;
  }
  .card {
    position: absolute;
    top: 293px;
    width: 540px;
    height: 309px;
    background: var(--card);
    box-shadow: 0 6px 18px rgba(0,0,0,0.18);
  }
  .card--front { left: 620px; }
  .card--back {
    left: 40px;
    background: var(--frame);
    padding: 14px;
  }
  .card__inner {
    position: relative;
    width: 100%;
    height: 100%;
    background: var(--card);
  }
  .brand {
    position: absolute;
    display: flex;
    flex-direction: column;
    align-items: center;
  }
  .brand__dot {
    width: 16px; height: 16px;
    border-radius: 50%;
    background: var(--accent);
    margin-bottom: 8px;
  }
  .brand__name {
    font-size: 44px;
    font-weight: 400;
    color: var(--ink);
    letter-spacing: 1px;
    line-height: 1;
  }
  .brand__tagline {
    margin-top: 8px;
    padding-bottom: 4px;
    border-bottom: 1px solid var(--rule);
    font-size: 12.5px;
    color: var(--muted);
    letter-spacing: 0.3px;
  }
  .card--front .brand { left: 0; right: 0; top: 92px; }
  .card--back .brand { left: 40px; top: 26px; }
  .card--back .brand__name { font-size: 38px; }
  .card--back .brand__tagline { font-size: 11px; }

  .clinic {
    position: absolute;
    left: 52px;
    top: 172px;
    font-size: 11.5px;
    line-height: 1.55;
    color: var(--ink);
  }
  .contact {
    position: absolute;
    left: 270px;
    top: 140px;
    font-size: 11.5px;
    line-height: 1.55;
  }
  .contact__name { color: var(--accent); font-weight: 600; font-size: 13px; }
  .contact__creds { color: var(--muted); margin-bottom: 10px; }
  .contact__list { list-style: none; }
  .contact__item { display: flex; align-items: center; gap: 7px; margin-bottom: 3px; }
  .contact__icon { width: 13px; height: 13px; flex: none; }
</style>
</head>
<body>

  <section class="card card--back" aria-label="Business card, contact side">
    <div class="card__inner">
      <div class="brand">
        <span class="brand__dot"></span>
        <span class="brand__name">Bright Ferns</span>
        <span class="brand__tagline">Natural Wellness &amp; Live Cell Review</span>
      </div>

      <address class="clinic" style="font-style: normal;">
        Larkvale Acupuncture Clinic<br>
        2736-18 Avenue, Suite 200<br>
        Larkvale, AB T8K 2P6
      </address>

      <div class="contact">
        <div class="contact__name">Marla Dunwoody</div>
        <div class="contact__creds">DynBC, CH, BA</div>
        <ul class="contact__list">
          <li class="contact__item">
            <svg class="contact__icon" viewBox="0 0 14 14"><circle cx="7" cy="7" r="7" fill="#3f8fd0"/><path d="M4.6 3.6l1.3 1.6-.7.9c.4.9 1 1.6 1.9 2.1l.9-.7 1.6 1.3-.6 1.2c-2.6-.3-4.7-2.4-5-5z" fill="#fff"/></svg>
            <span>780 555 0148</span>
          </li>
          <li class="contact__item">
            <svg class="contact__icon" viewBox="0 0 14 14"><circle cx="7" cy="7" r="7" fill="#3f8fd0"/><rect x="3.5" y="4.5" width="7" height="5" fill="none" stroke="#fff" stroke-width="1"/><path d="M3.5 4.5l3.5 2.8 3.5-2.8" fill="none" stroke="#fff" stroke-width="1"/></svg>
            <span>brightferns@mailnest.ca</span>
          </li>
          <li class="contact__item">
            <svg class="contact__icon" viewBox="0 0 14 14"><circle cx="7" cy="7" r="7" fill="#3f8fd0"/><circle cx="7" cy="7" r="3.6" fill="none" stroke="#fff" stroke-width="0.9"/><ellipse cx="7" cy="7" rx="1.5" ry="3.6" fill="none" stroke="#fff" stroke-width="0.9"/><path d="M3.4 7h7.2" stroke="#fff" stroke-width="0.9"/></svg>
            <span>www.brightfernsnaturalwellness.com</span>
          </li>
        </ul>
      </div>
    </div>
  </section>

  <section class="card card--front" aria-label="Business card, brand side">
    <div class="brand">
      <span class="brand__dot"></span>
      <span class="brand__name">Bright Ferns</span>
      <span class="brand__tagline">Natural Wellness &amp; Live Cell Review</span>
    </div>
  </section>

</body>
</html>
```